Vellora - Quality health delivered at your door

Vellora offers home and Community Based Services for adults who wish to continue live independently in their communities. We increase accessibility to health care, reduce health care delivery gap, reduce mortality and morbidity, reduce health while promoting healthy living in the comfort of our patients communities or homes.

We provide on site services and deliver high quality healthcare at your door. Our experienced physicians coordinate care with our certified nurse practitioners and provide chronic care management, physical therapy, rehabilitation and medications management.

Target Market(s)

Older population living in independent living facilities

Industry/Entity Type

Health Care

Contact Information for Business Card

Vellora

Number of Pages Required

4 page

Font styles to use
Sans Serif

Colors

Designer to choose colors to be used in the design.

```html
<!DOCTYPE html>
<html lang="en">
<head>
<meta charset="utf-8">
<title>Vellora - Quality health delivered at your door</title>
<link href="https://fonts.googleapis.com/css2?family=Open+Sans:wght@400;600;700;800&display=swap" rel="stylesheet">
<style>
:root{
  --green:#4e6d1a;
  --green-dark:#3f5a12;
  --orange:#f59c00;
  --ink:#333;
  --muted:#777;
  --line:#e3e3e3;
  --footer:#262626;
  --footer-deep:#1b1b1b;
  --white:#fff;
}
*{box-sizing:border-box;margin:0;padding:0}
html,body{width:1200px;height:3264px;overflow:hidden}
body{font-family:"Open Sans",Arial,sans-serif;color:var(--ink);background:var(--white);position:relative}
section,header,footer,nav{position:absolute;left:0;width:1200px}

/* header */
.topbar{top:0;height:120px;display:flex;align-items:center;padding:0 72px}
.brand{display:flex;align-items:center;gap:14px;font-size:30px;font-weight:700;color:var(--green);letter-spacing:1px}
.brand-dot{width:44px;height:44px;border-radius:50%;background:var(--orange)}
.contacts{margin-left:auto;display:flex;gap:46px}
.contact{display:flex;align-items:center;gap:12px;font-size:15px;line-height:20px;color:#555}
.contact svg{width:34px;height:34px;flex:none}

.mainnav{top:120px;height:48px;background:var(--green);display:flex;align-items:center;padding:0 40px;overflow:hidden}
.mainnav a{color:var(--white);text-decoration:none;font-size:12px;font-weight:700;padding:0 13px;line-height:48px;white-space:nowrap}
.mainnav a.active{background:var(--orange)}

/* hero */
.hero{top:168px;height:552px;overflow:hidden}
.hero-photo{position:absolute;inset:0;background:linear-gradient(110deg,#6f8a4a 0%,#b7b0a2 30%,#d9cfc4 50%,#8ba46a 75%,#5f7c35 100%)}
.hero-badge{position:absolute;left:690px;top:30px;width:580px;height:580px;border-radius:50%;background:var(--orange);opacity:.95}
.hero-copy{position:absolute;left:750px;top:130px;width:400px;color:var(--white)}
.hero-copy h1{font-size:34px;line-height:42px;font-weight:800}
.hero-copy p{margin-top:18px;font-size:14px;line-height:21px;width:360px}
.more{position:absolute;left:990px;top:400px;width:124px;height:124px;border-radius:50%;background:var(--green);color:var(--white);font-weight:800;font-size:16px;line-height:20px;text-align:center;display:flex;align-items:center;justify-content:center}

/* welcome */
.welcome{top:720px;height:600px;text-align:center}
.section-title{font-size:46px;font-weight:400;color:#2c2c2c}
.welcome .section-title{margin-top:50px}
.rule{width:840px;height:1px;background:var(--line);margin:18px auto 0}
.welcome .intro{width:1060px;margin:22px auto 0;font-size:15px;line-height:24px;color:var(--muted)}
.features{display:flex;justify-content:center;gap:100px;margin-top:50px}
.feature{width:260px}
.feature-icon{width:88px;height:88px;margin:0 auto;background:var(--orange);display:flex;align-items:center;justify-content:center}
.feature h3{margin-top:14px;font-size:22px;font-weight:600;color:#2c2c2c}
.feature p{margin-top:12px;font-size:14px;line-height:22px;color:var(--muted)}
.slide-arrow{position:absolute;top:362px;width:20px;height:30px}

/* services */
.services{top:1320px;height:340px;background:var(--green)}
.services-photo{position:absolute;left:0;top:0;width:560px;height:340px;background:linear-gradient(120deg,#7c8f4a,#d8c3a8 45%,#c9b6a0 70%,#6a7d38)}
.services-copy{position:absolute;left:590px;top:56px;width:560px;color:var(--white)}
.services-copy h2{font-size:26px;font-weight:700}
.services-copy p{margin-top:16px;font-size:15px;line-height:23px}
.btn{display:inline-block;background:var(--white);color:var(--green);font-weight:700;font-size:15px;padding:10px 22px;margin-top:22px}

/* blog */
.blog{top:1660px;height:800px;text-align:center}
.blog .section-title{margin-top:88px;font-weight:600;font-size:44px}
.blog-title-row{display:flex;align-items:center;justify-content:center;gap:24px}
.blog-title-row span{width:300px;height:1px;background:var(--line)}
.cards{position:absolute;top:184px;left:72px;display:flex;gap:24px}
.card{width:336px;height:476px;border:1px solid var(--line);text-align:left;position:relative;background:var(--white)}
.card-photo{height:208px}
.card:nth-child(1) .card-photo{background:linear-gradient(120deg,#a58a6c,#d9c5ae 55%,#6e8a4e)}
.card:nth-child(2) .card-photo{background:linear-gradient(120deg,#cfc4b8,#e6ddd3 50%,#b59a82)}
.card:nth-child(3) .card-photo{background:linear-gradient(120deg,#6b8f4a,#d4c0a6 50%,#8aa664)}
.card-tag{position:absolute;right:22px;top:178px;width:60px;height:60px;border-radius:50%;background:var(--orange);display:flex;align-items:center;justify-content:center}
.card-body{padding:40px 28px 0}
.card h3{font-size:20px;font-weight:700;color:var(--green)}
.card .meta{margin-top:8px;font-size:13px;color:#999}
.card .meta b{color:#555;font-weight:600;margin-right:18px}
.card p{margin-top:16px;font-size:14px;line-height:22px;color:var(--muted)}
.btn-green{position:absolute;left:528px;top:680px;background:var(--green);color:var(--white);font-size:14px;font-weight:600;padding:10px 24px}

/* contact */
.touch{top:2460px;height:420px}
.touch h2{position:absolute;left:56px;top:60px;font-size:30px;font-weight:700;color:#2c2c2c}
.form{position:absolute;left:56px;top:118px;width:376px}
.field{height:42px;border:1px solid #ccc;margin-bottom:12px;font-size:14px;color:#999;padding:11px 12px}
.field.tall{height:88px}
.submit{height:46px;background:var(--green);color:var(--white);font-weight:600;font-size:15px;text-align:center;line-height:46px}
.touch-photo{position:absolute;left:520px;top:0;width:680px;height:420px;background:linear-gradient(100deg,#fff 0%,#eee 30%,#bdbdbd 60%,#8d8d8d 100%)}

/* footer */
.site-footer{top:2880px;height:384px;background:var(--footer);color:#ddd}
.footer-col{position:absolute;top:70px}
.footer-col h4{font-size:15px;font-weight:700;color:var(--white);letter-spacing:.5px}
.nav-lists{display:flex;gap:70px;margin-top:30px}
.nav-lists ul{list-style:none}
.nav-lists li{font-size:14px;line-height:30px}
.contact-list{margin-top:26px}
.contact-list .row{display:flex;gap:14px;align-items:flex-start;font-size:13px;line-height:18px;margin-bottom:18px}
.pin{width:28px;height:28px;border-radius:50%;background:var(--orange);flex:none;display:flex;align-items:center;justify-content:center}
.map{position:absolute;left:860px;top:100px;width:280px;height:190px;background:linear-gradient(135deg,#e8e4d8,#d4dcc6 50%,#e6e1d2)}
.copyright{position:absolute;left:0;top:332px;width:1200px;height:52px;background:var(--footer-deep);text-align:center;line-height:52px;font-size:13px;color:#999}
</style>
</head>
<body>

<header class="topbar">
  <div class="brand"><span class="brand-dot"></span>VELLORA</div>
  <div class="contacts">
    <div class="contact">
      <svg viewBox="0 0 34 34"><circle cx="17" cy="17" r="17" fill="#f59c00"/><path d="M12 9l4 4-2 2c1 3 3 5 6 6l2-2 4 4-3 3c-7 0-14-7-14-14z" fill="#fff"/></svg>
      <div>0800 555 0142<br>hello@vellora-care.com</div>
    </div>
    <div class="contact">
      <svg viewBox="0 0 34 34"><circle cx="17" cy="17" r="17" fill="#f59c00"/><path d="M17 8a6 6 0 0 1 6 6c0 5-6 12-6 12s-6-7-6-12a6 6 0 0 1 6-6z" fill="#fff"/><circle cx="17" cy="14" r="2.3" fill="#f59c00"/></svg>
      <div>18 Orchard Lane<br>Brookfield, NY 10016</div>
    </div>
    <div class="contact">
      <svg viewBox="0 0 34 34"><circle cx="17" cy="17" r="17" fill="#f59c00"/><circle cx="17" cy="17" r="9" fill="none" stroke="#fff" stroke-width="2"/><path d="M17 11v6l4 3" stroke="#fff" stroke-width="2" fill="none"/></svg>
      <div>7:30 AM - 7:30 PM<br>Monday to Saturday</div>
    </div>
  </div>
</header>

<nav class="mainnav">
  <a class="active">HOME</a><a>ASSISTED LIVING</a><a>SKILLED NURSING</a><a>INDEPENDENT LIVING</a><a>RESPITE CARE</a><a>REHABILITATION</a><a>HEALTH LEARNING</a><a>HEALTHY LIVING</a>
</nav>

<section class="hero">
  <div class="hero-photo" role="img" aria-label="Photo of a carer with a smiling senior woman in a wheelchair in a garden"></div>
  <div class="hero-badge"></div>
  <div class="hero-copy">
    <h1>YOU CAN'T ALWAYS<br>BE THERE BUT WE CAN</h1>
    <p>Caring nurses and physicians bring trusted health support to your home, so loved ones stay safe and independent.</p>
  </div>
  <div class="more">MORE<br>DETAILS</div>
</section>

<section class="welcome">
  <h2 class="section-title">Welcome to Vellora</h2>
  <div class="rule"></div>
  <p class="intro">We provide on site services and deliver high quality healthcare at your door. Our experienced physicians coordinate care with our certified nurse practitioners and provide chronic care management, physical therapy, rehabilitation and medications management.</p>
  <svg class="slide-arrow" style="left:24px" viewBox="0 0 20 30"><path d="M16 3L4 15l12 12" stroke="#333" stroke-width="4" fill="none"/></svg>
  <svg class="slide-arrow" style="right:24px" viewBox="0 0 20 30"><path d="M4 3l12 12L4 27" stroke="#333" stroke-width="4" fill="none"/></svg>
  <div class="features">
    <div class="feature">
      <div class="feature-icon"><svg width="48" height="48" viewBox="0 0 48 48"><path d="M24 40S6 29 6 17a9 9 0 0 1 18-3 9 9 0 0 1 18 3c0 12-18 23-18 23z" fill="#fff"/></svg></div>
      <h3>Mental health</h3>
      <p>Gentle, regular support for emotional wellbeing, memory and mood, delivered by caring specialists at home.</p>
    </div>
    <div class="feature">
      <div class="feature-icon"><svg width="48" height="48" viewBox="0 0 48 48"><path d="M14 6c4 0 6 2 10 2s6-2 10-2c6 0 8 6 7 12-1 5-3 8-4 14-1 6-2 10-5 10s-3-10-8-10-5 10-8 10-4-4-5-10c-1-6-3-9-4-14C6 12 8 6 14 6z" fill="#fff"/></svg></div>
      <h3>Dental health</h3>
      <p>Routine checks and cleaning at your door, helping you keep a healthy, comfortable smile for life.</p>
    </div>
    <div class="feature">
      <div class="feature-icon"><svg width="48" height="48" viewBox="0 0 48 48"><circle cx="24" cy="9" r="5" fill="#fff"/><path d="M24 16v14M12 22h24M24 30l-8 12M24 30l8 12" stroke="#fff" stroke-width="5" stroke-linecap="round"/></svg></div>
      <h3>Physical therapy</h3>
      <p>Guided exercises and rehabilitation that rebuild strength, balance and mobility in familiar surroundings.</p>
    </div>
  </div>
</section>

<section class="services">
  <div class="services-photo" role="img" aria-label="Photo of a young woman hugging a smiling senior woman"></div>
  <div class="services-copy">
    <h2>Our Services Vellora</h2>
    <p>We provide the finest community health services across the region, and there is no charge when we visit to plan your care.</p>
    <p>We are committed to helping you live well at home, with clear plans, friendly visits and support for the whole family.</p>
    <span class="btn">Read More &rsaquo;</span>
  </div>
</section>

<section class="blog">
  <div class="blog-title-row"><span></span><h2 class="section-title">Latest Blog</h2><span></span></div>
  <div class="cards">
    <article class="card">
      <div class="card-photo" role="img" aria-label="Photo of seniors doing a puzzle together"></div>
      <div class="card-tag"><svg width="26" height="26" viewBox="0 0 26 26"><rect x="3" y="5" width="20" height="16" rx="2" fill="#fff"/><rect x="6" y="9" width="14" height="2" fill="#f59c00"/><rect x="6" y="14" width="10" height="2" fill="#f59c00"/></svg></div>
      <div class="card-body">
        <h3>In-Home Senior Care</h3>
        <div class="meta"><b>M. Harlow</b>24 May 2017</div>
        <p>Simple routines, friendly company and regular checks help older adults stay active and well at home.</p>
      </div>
    </article>
    <article class="card">
      <div class="card-photo" role="img" aria-label="Photo of a nurse with a senior couple"></div>
      <div class="card-tag"><svg width="26" height="26" viewBox="0 0 26 26"><rect x="3" y="5" width="20" height="16" rx="2" fill="#fff"/><rect x="6" y="9" width="14" height="2" fill="#f59c00"/><rect x="6" y="14" width="10" height="2" fill="#f59c00"/></svg></div>
      <div class="card-body">
        <h3>In-Home Senior Care</h3>
        <div class="meta"><b>M. Harlow</b>24 May 2017</div>
        <p>Simple routines, friendly company and regular checks help older adults stay active and well at home.</p>
      </div>
    </article>
    <article class="card">
      <div class="card-photo" role="img" aria-label="Photo of a carer and senior outdoors"></div>
      <div class="card-tag"><svg width="26" height="26" viewBox="0 0 26 26"><rect x="3" y="5" width="20" height="16" rx="2" fill="#fff"/><rect x="6" y="9" width="14" height="2" fill="#f59c00"/><rect x="6" y="14" width="10" height="2" fill="#f59c00"/></svg></div>
      <div class="card-body">
        <h3>In-Home Senior Care</h3>
        <div class="meta"><b>M. Harlow</b>24 May 2017</div>
        <p>Simple routines, friendly company and regular checks help older adults stay active and well at home.</p>
      </div>
    </article>
  </div>
  <span class="btn-green">View all news &rsaquo;</span>
</section>

<section class="touch">
  <div class="touch-photo" role="img" aria-label="Greyscale photo of a hand using a calculator and pen on paperwork"></div>
  <h2>Get in Touch</h2>
  <div class="form">
    <div class="field">Name</div>
    <div class="field">Email address</div>
    <div class="field tall">Message</div>
    <div class="submit">Submit</div>
  </div>
</section>

<footer class="site-footer">
  <div class="footer-col" style="left:80px">
    <h4>NAVIGATION</h4>
    <div class="nav-lists">
      <ul><li>Home</li><li>About</li><li>Services</li><li>Rates</li><li>Collection Process</li></ul>
      <ul><li>Privacy policy</li><li>Contact</li><li>Forms</li><li>Blog</li></ul>
    </div>
  </div>
  <div class="footer-col" style="left:446px">
    <h4>CONTACT DETAILS</h4>
    <div class="contact-list">
      <div class="row"><span class="pin"><svg width="14" height="14" viewBox="0 0 14 14"><path d="M7 1a4 4 0 0 1 4 4c0 3-4 8-4 8S3 8 3 5a4 4 0 0 1 4-4z" fill="#fff"/></svg></span><div><b>VELLORA</b><br>18 Orchard Lane<br>Brookfield, NY 10016</div></div>
      <div class="row"><span class="pin"><svg width="14" height="14" viewBox="0 0 14 14"><path d="M3 1l3 3-1.5 1.5c1 2 2 3 4 4L10 8l3 3-2 2C6 13 1 8 1 3z" fill="#fff"/></svg></span><div>0800 555 0142</div></div>
      <div class="row"><span class="pin"><svg width="14" height="14" viewBox="0 0 14 14"><rect x="1" y="3" width="12" height="8" fill="#fff"/><path d="M1 3l6 5 6-5" stroke="#f59c00" fill="none"/></svg></span><div>hello@vellora-care.com</div></div>
    </div>
  </div>
  <div class="map" role="img" aria-label="Street map showing the office location"></div>
  <div class="copyright">Copyright &copy; 2017 Vellora. All Rights Reserved</div>
</footer>

</body>
</html>
```